Brindlewood Orthopaedic logo and letterhead

Letterhead AND LOGO rediesign for a surgical medical practice located in Australia.
LOGO - should have an upper limb, shoulder, joint or convey movement
General feel is business/professional. Layout should allow as much space for text as possible
Include the information that is on the proof below that is the current letter head
Need designs in .dotx template and .pdf

Target Market(s)

general practitioner doctors

Industry/Entity Type

medical

Font styles to use
Sans Serif

Colors
0054AA
0677BA
7BADD7
CADEEF
E8F1F8

```html
<!DOCTYPE html>
<html lang="en">
<head>
<meta charset="utf-8">
<title>Brindlewood Orthopaedics — Stationery</title>
<link href="https://fonts.googleapis.com/css2?family=Montserrat:wght@600;700;800&family=Roboto:wght@400;500;700&display=swap" rel="stylesheet">
<style>
  :root{
    --brand-deep:#0054AA;
    --brand-mid:#0677BA;
    --brand-soft:#7BADD7;
    --brand-pale:#CADEEF;
    --brand-mist:#E8F1F8;
    --ink:#111111;
    --grey:#5a5a5a;
    --paper:#ffffff;
  }
  *{box-sizing:border-box;margin:0;padding:0}
  html,body{width:1200px;height:1200px;overflow:hidden;background:var(--paper)}
  body{position:relative;font-family:"Roboto",Arial,sans-serif;color:var(--ink)}

  .card-stage{position:absolute;left:0;top:0;width:1200px;height:428px;
    background:linear-gradient(180deg,#f3f6fb 0%,#dde8f8 45%,#9ec0f3 100%)}
  .card{position:absolute;top:98px;width:451px;height:271px;background:var(--paper);
    box-shadow:0 2px 8px rgba(30,60,120,.18);overflow:hidden}
  .card--front{left:134px}
  .card--back{left:617px}

  .wordmark{display:flex;flex-direction:column;align-items:center;color:var(--brand-deep);
    font-family:"Montserrat",Arial,sans-serif;font-weight:800;line-height:1}
  .wordmark__dot{width:68px;height:68px;border-radius:50%;background:var(--brand-deep);margin-bottom:12px}
  .wordmark__name{font-size:27px;letter-spacing:.3px;white-space:nowrap}
  .wordmark__sub{font-size:10px;letter-spacing:1.6px;margin-top:7px}

  .card--front .wordmark{position:absolute;top:74px;left:58px;width:300px}
  .spine-decor{position:absolute;background:linear-gradient(180deg,var(--brand-mist),#f1f5fa)}
  .card--front .spine-decor{right:0;top:0;width:110px;height:271px;border-radius:60px 0 0 60px}

  .card__person{position:absolute;left:0;width:100%;top:118px;text-align:center}
  .person-name{font-family:"Montserrat",Arial,sans-serif;font-weight:700;color:var(--brand-deep);white-space:nowrap}
  .card__person .person-name{font-size:18px}
  .card__person .person-role{font-size:11px;color:var(--grey);margin-top:5px}
  .card__band{position:absolute;left:0;bottom:0;width:100%;height:93px;background:var(--brand-deep);
    color:#fff;text-align:center;padding:26px 0 0 48px}
  .card__band .spine-decor{left:0;top:0;width:42px;height:93px;border-radius:0 30px 30px 0;
    background:linear-gradient(180deg,#2b6fbd,#1f63b4)}
  .band-address{font-family:"Montserrat",Arial,sans-serif;font-weight:700;font-size:10px;white-space:nowrap}
  .band-contacts{font-size:9.4px;margin-top:5px;white-space:nowrap}
  .band-contacts b{font-weight:700}

  .letterhead{position:absolute;left:370px;top:462px;width:480px;height:680px;background:var(--paper);
    box-shadow:0 6px 26px rgba(0,0,0,.16),0 1px 3px rgba(0,0,0,.12);overflow:hidden}
  .letterhead__logo-box{position:absolute;right:0;top:0;width:120px;height:92px;background:var(--brand-mist);
    display:flex;align-items:center;justify-content:center}
  .letterhead__logo-box .wordmark__dot{width:22px;height:22px;margin-bottom:5px}
  .letterhead__logo-box .wordmark__name{font-size:11px}
  .letterhead__logo-box .wordmark__sub{font-size:5px;letter-spacing:.8px;margin-top:3px}
  .letterhead__sender{position:absolute;left:34px;top:38px}
  .letterhead__sender .person-name{font-size:17px}
  .letterhead__sender .person-role{font-size:6.5px;color:#333;margin-top:4px;line-height:1.45}
  .letterhead .spine-decor{left:0;top:355px;width:140px;height:325px;border-radius:0 70px 0 0;
    background:linear-gradient(180deg,#f0f5fa,#f3f7fb)}
  .letterhead__footer{position:absolute;left:34px;bottom:28px;color:var(--brand-deep)}
  .footer-address{font-family:"Montserrat",Arial,sans-serif;font-weight:700;font-size:9.5px;white-space:nowrap}
  .footer-contacts{font-size:7.5px;margin-top:4px;color:var(--brand-soft);white-space:nowrap}
  .footer-contacts b{color:var(--brand-deep);font-weight:700}
  .messaging-pill{position:absolute;right:0;bottom:150px;width:142px;height:22px;border-radius:11px 0 0 11px;
    background:var(--brand-deep);color:#fff;font-size:6.5px;font-weight:500;letter-spacing:.3px;
    display:flex;align-items:center;justify-content:center;text-transform:uppercase;white-space:nowrap}

  .standalone-logo{position:absolute;left:900px;top:478px;width:220px}
  .standalone-logo .wordmark__name{font-size:27px}

  .caption{position:absolute;left:0;top:1103px;width:340px;text-align:center;white-space:nowrap;
    font-family:"Montserrat",Arial,sans-serif;font-weight:800;font-size:19px;line-height:1.15;color:#000}
</style>
</head>
<body>

<section class="card-stage">
  <article class="card card--front">
    <div class="wordmark">
      <span class="wordmark__dot"></span>
      <span class="wordmark__name">BRINDLEWOOD</span>
      <span class="wordmark__sub">ORTHOPAEDICS</span>
    </div>
    <div class="spine-decor" role="img" aria-label="Faint spine illustration running down the card edge"></div>
  </article>

  <article class="card card--back">
    <div class="card__person">
      <div class="person-name">Daniel Ashcombe</div>
      <div class="person-role">MBBS, FRACS, Orthopaedic Surgeon, 48210KM</div>
    </div>
    <div class="card__band">
      <div class="spine-decor" role="img" aria-label="Spine illustration at the band edge"></div>
      <div class="band-address">Suite 14, Level 2 Harbourview Private Hospital, Brindlewood Vic 3062</div>
      <div class="band-contacts"><b>Ph:</b> 95550142 &nbsp;|&nbsp; <b>Fax:</b> 85550177 &nbsp;|&nbsp; <b>Email:</b> info@danashcombe.com.au</div>
    </div>
  </article>
</section>

<article class="letterhead">
  <div class="letterhead__logo-box">
    <div class="wordmark">
      <span class="wordmark__dot"></span>
      <span class="wordmark__name">BRINDLEWOOD</span>
      <span class="wordmark__sub">ORTHOPAEDICS</span>
    </div>
  </div>
  <div class="letterhead__sender">
    <div class="person-name">Daniel Ashcombe</div>
    <div class="person-role">MBBS, FRACS,<br>Orthopaedic Surgeon, 48210KM</div>
  </div>
  <div class="spine-decor" role="img" aria-label="Faint spine illustration along the lower left of the page"></div>
  <div class="messaging-pill">We accept Medlink Messaging</div>
  <div class="letterhead__footer">
    <div class="footer-address">Suite 14, Level 2 Harbourview Private Hospital, Brindlewood Vic 3062</div>
    <div class="footer-contacts"><b>Ph:</b> 95550142 &nbsp;|&nbsp; <b>Fax:</b> 85550177 &nbsp;|&nbsp; <b>Email:</b> info@danashcombe.com.au</div>
  </div>
</article>

<div class="standalone-logo">
  <div class="wordmark">
    <span class="wordmark__dot"></span>
    <span class="wordmark__name">BRINDLEWOOD</span>
    <span class="wordmark__sub">ORTHOPAEDICS</span>
  </div>
</div>

<p class="caption">LETTERHEAD, BUSINESS CARD<br>&amp; LOGO DESIGN<br>-2</p>

</body>
</html>
```